Kveldbrá - Start-up company selling electricity

Hello let me tell you about Kveldbrá.

Kveldbrá is start-up company selling electricity in Iceland. The operations of the company consist of making power usage forecasts for our customers, purchasing the electricity wholesale from the energy producers, and selling the electricity to the consumer. We are focused on tech by using optimization and machine learning to minimize electricity prices to our customers. Our marketing strategy is to portray a tech company mindset and to show dedication to driving down the electricity price on the market.

We need your help to make our website pop. Possible concepts to work with are as follows:

- Iceland the land of ice and fire
- Green energy
- Innovation
- Tech and data science

Link to our website: https://prufa.kveldbra.is/
We are open to ideas.
Thank you!

Target Market(s)

Electricity consumers both homes and companies.

Number of Pages Required

1 page

Font styles to use
Serif
Sans Serif

```html
<!DOCTYPE html>
<html lang="is">
<head>
<meta charset="utf-8">
<title>Kveldbrá – Sama rafmagn, bara ódýrara</title>
<link rel="stylesheet" href="https://fonts.googleapis.com/css2?family=Roboto:wght@400;500;700&family=Roboto+Condensed:wght@700&family=Fira+Sans:wght@400;500&display=swap">
<style>
:root{
  --navy:#142e55;
  --red:#a2281f;
  --card:#e6e6e6;
  --ink:#111;
  --footer:#1b1b1b;
  --white:#fff;
}
*{box-sizing:border-box;margin:0;padding:0}
html,body{width:827px;height:1200px;overflow:hidden}
body{position:relative;font-family:"Roboto",sans-serif;color:var(--ink);background:var(--white)}

.site-header{position:absolute;left:0;top:0;width:827px;height:52px;background:var(--white)}
.brand{position:absolute;left:17px;top:13px;display:flex;align-items:center;gap:7px}
.brand-dot{width:22px;height:22px;border-radius:50%;background:var(--navy)}
.brand-name{font:700 22px "Roboto",sans-serif;color:var(--red);letter-spacing:.5px}
.main-nav a{position:absolute;top:20px;font-size:8.5px;font-weight:500;color:var(--ink);text-decoration:none}
.main-nav a.active::after{content:"";position:absolute;left:0;right:0;top:27px;height:3px;background:var(--red)}

.hero{position:absolute;left:0;top:52px;width:827px;height:413px;
  background:radial-gradient(ellipse 260px 70px at 50% 48%,#3b6fd8 0%,#1b2f6a 40%,transparent 75%),
  linear-gradient(180deg,#07080d 0%,#101528 55%,#0d1630 100%)}
.hero-title{position:absolute;left:0;width:827px;text-align:center;font:700 34px "Roboto Condensed",sans-serif;color:var(--white);letter-spacing:.5px}

.card{position:absolute;top:421px;width:179px;height:230px;background:var(--card);border-radius:4px;text-align:center}
.card-icon{position:absolute;left:61px;top:16px;width:57px;height:57px;border-radius:50%;background:var(--navy);display:flex;align-items:center;justify-content:center}
.card-title{position:absolute;left:0;right:0;top:90px;font-size:13px;font-weight:700;line-height:16px}
.btn{position:absolute;left:43px;width:93px;height:23px;border-radius:12px;color:var(--white);font-size:11.5px;letter-spacing:.3px;display:flex;align-items:center;justify-content:center}
.btn-red{background:var(--red)}
.btn-navy{background:var(--navy)}
.prices{position:absolute;left:14px;right:14px;top:114px;height:51px;border-top:1px solid #d6d6d6;border-bottom:1px solid #d6d6d6;display:flex}
.price{flex:1;display:flex;flex-direction:column;justify-content:center;font-size:7.5px;line-height:9px}
.price + .price{border-left:1px solid #d6d6d6}
.price strong{font-weight:400;font-size:18px;line-height:18px}
.card-note{position:absolute;left:12px;right:12px;font-size:8px;line-height:12.7px}

.contact{position:absolute;left:0;top:693px;width:827px;height:439px;background:var(--navy)}
.contact-art{position:absolute;left:57px;top:42px;width:456px;height:353px;border-radius:6px;
  background:linear-gradient(160deg,#8fa9d3 0%,#c9d8f2 35%,#6f9a3a 60%,#1f3766 100%);opacity:.9}
.contact-title{position:absolute;left:548px;top:62px;font:500 31px "Fira Sans",sans-serif;color:var(--white);letter-spacing:3px}
.field{position:absolute;left:549px;width:189px;background:var(--white);border-radius:6px;font:400 13px "Fira Sans",sans-serif;color:#c3c3c3;letter-spacing:1px;padding:7px 10px}
.submit{position:absolute;left:549px;top:312px;width:189px;height:29px;border-radius:6px;background:var(--red);color:var(--white);font:500 20px "Fira Sans",sans-serif;letter-spacing:2.5px;display:flex;align-items:center;justify-content:center}

.site-footer{position:absolute;left:0;top:1132px;width:827px;height:68px;background:var(--footer);color:var(--white);font-size:8px;line-height:12px}
.footer-company{position:absolute;left:117px;top:15px}
.footer-copy{position:absolute;left:284px;width:200px;top:21px;text-align:center}
.footer-contact{position:absolute;left:570px;top:13px;list-style:none}
.footer-contact li{display:flex;align-items:center;gap:6px;height:13.5px}
.footer-contact .ico{width:11px;height:11px;border-radius:50%;background:var(--red);display:flex;align-items:center;justify-content:center}
</style>
</head>
<body>

<header class="site-header">
  <div class="brand"><span class="brand-dot"></span><span class="brand-name">KVELDBRÁ</span></div>
  <nav class="main-nav">
    <a class="active" style="left:569px">Viðskiptaskilmálar</a>
    <a style="left:664px">Spurt &amp; svarað</a>
    <a style="left:744px">Um Kveldbrá</a>
  </nav>
</header>

<section class="hero" role="img" aria-label="Two electric cable ends joined by a bright blue electric arc on a dark background">
  <h1 class="hero-title" style="top:131px">SAMA RAFMAGN</h1>
  <h1 class="hero-title" style="top:230px">BARA ÓDÝRARA!</h1>
</section>

<article class="card" style="left:117px">
  <div class="card-icon">
    <svg width="22" height="30" viewBox="0 0 22 30" fill="none" stroke="#fff" stroke-width="2" stroke-linecap="round" stroke-linejoin="round"><path d="M7 2v7M15 2v7M3 9h16v6a8 8 0 0 1-16 0z"/><path d="M11 23v5"/></svg>
  </div>
  <h2 class="card-title">VELKOMIN Í<br>VIÐSKIPTI</h2>
  <div class="btn btn-red" style="top:135px">FYRIRTÆKI</div>
  <div class="btn btn-navy" style="top:168px">HEIMILI</div>
</article>

<article class="card" style="left:324px">
  <div class="card-icon">
    <svg width="30" height="26" viewBox="0 0 30 26" fill="none" stroke="#fff" stroke-width="2" stroke-linejoin="round"><path d="M2 14 12 3h12v10"/><circle cx="19" cy="7" r="1.4" fill="#fff"/><ellipse cx="21" cy="16" rx="6" ry="2.5"/><path d="M15 16v6c0 1.4 2.7 2.5 6 2.5s6-1.1 6-2.5v-6"/><path d="M15 19c0 1.4 2.7 2.5 6 2.5s6-1.1 6-2.5"/><path d="M2 14l6 6h6"/></svg>
  </div>
  <h2 class="card-title">VERÐSKRÁ</h2>
  <div class="prices">
    <div class="price"><strong>6.95</strong>krónur / kWst</div>
    <div class="price"><strong>6.22</strong>krónur / kWst<br>rafmagnskynding</div>
  </div>
  <p class="card-note" style="top:170px">Gerðu verðsamanburð</p>
  <div class="btn btn-navy" style="top:188px">VERÐVITI</div>
</article>

<article class="card" style="left:531px">
  <div class="card-icon">
    <svg width="22" height="30" viewBox="0 0 22 30" fill="none" stroke="#fff" stroke-width="2" stroke-linejoin="round"><path d="M13 2 3 17h8l-3 11 11-16h-8z"/></svg>
  </div>
  <h2 class="card-title">FRAMTÍÐIN ER<br>SPENNANDI</h2>
  <p class="card-note" style="top:128px">Gerum raforkukerfið snallara saman.<br>Kveldbrá notar gervigreind, gagnavísindi<br>og sjálfvirkni til að lágmarka kostnað og<br>stuðla að okrujöfnuði</p>
  <div class="btn btn-navy" style="top:188px">VERÐVITI</div>
</article>

<section class="contact">
  <div class="contact-art" role="img" aria-label="Illustration of a person working on a laptop in an armchair beside a plant, a lamp and a side table"></div>
  <h2 class="contact-title">CONTACT US</h2>
  <div class="field" style="top:107px;height:29px">Name</div>
  <div class="field" style="top:150px;height:29px">Email</div>
  <div class="field" style="top:196px;height:101px">Message</div>
  <div class="submit">SUBMIT</div>
</section>

<footer class="site-footer">
  <div class="footer-company">Kveldbrá ehf<br>Kennitala: 010101-0190<br>Vskm númer: 100200</div>
  <div class="footer-copy">Copyright © Kveldbrá 2020<br>Allur réttur áskilin</div>
  <ul class="footer-contact">
    <li><span class="ico"><svg width="6" height="7" viewBox="0 0 6 7"><path d="M3 7 .8 3.6A2.4 2.4 0 1 1 5.2 3.6z" fill="none" stroke="#fff" stroke-width=".8"/></svg></span>Lindargata 7 600 Akureyri</li>
    <li><span class="ico"><svg width="6" height="5" viewBox="0 0 6 5"><rect x=".4" y=".4" width="5.2" height="4.2" fill="none" stroke="#fff" stroke-width=".8"/><path d="M.4.4 3 2.8 5.6.4" fill="none" stroke="#fff" stroke-width=".8"/></svg></span>kveldbra@kveldbra.is</li>
    <li><span class="ico"><svg width="6" height="6" viewBox="0 0 6 6"><path d="M1 .5 2.3 1.8 1.6 2.6A4 4 0 0 0 3.4 4.4l.8-.7L5.5 5 4.8 5.6A4.6 4.6 0 0 1 .4 1.2z" fill="#fff"/></svg></span>555-0199</li>
  </ul>
</footer>

</body>
</html>
```